Business Card Design

I need a business card for my resume writing business. I have a logo that Im not keen on anymore so I would like the business card to use my photo instead of a logo. I am for mid career and trades resumes and prefer not to do executive resumes so don't need to aim for exectives. I would like it to be colourful. I like bright sky blue and maybe some pink or purple but primarily bright sky blue. I don't like green and Im keen see a fair bit of white on the card. As I have a photo to go it, it will need to go on a white background.

Target Market(s)

mid range careers. Not executives

Industry/Entity Type

Business

Contact Information for Business Card

Wyn Marchetti
Resume Writer
Clear Path CVs
27 The Lanyard
HARWOOD NSW 2465
wyn@clearpathcvs.com.au
0417362958
www.clearpathcvs.com.au

Requirements
Nice to have
• Maybe colours similar to my website - www.clearpathcvs.com.au but not with any black on it.
Should not have
• No green or dark colours

```html
<!DOCTYPE html>
<html lang="en">
<head>
<meta charset="utf-8">
<title>Wyn Marchetti – Business Card</title>
<link rel="stylesheet" href="https://fonts.googleapis.com/css2?family=Source+Sans+3:wght@400;600;700&display=swap">
<style>
  :root {
    --sky: #009fe3;
    --ink: #4a4a4a;
    --paper: #ffffff;
    --backdrop: #e4e6e8;
    --photo-light: #f1ece8;
    --photo-mid: #c9a48c;
    --photo-dark: #3b2a24;
  }
  * { box-sizing: border-box; margin: 0; padding: 0; }
  html, body {
    width: 1200px; height: 1000px; overflow: hidden;
    background: var(--backdrop);
    font-family: "Source Sans 3", "Myriad Pro", Arial, sans-serif;
  }
  .stage {
    width: 1200px; height: 1000px;
    display: flex; align-items: center; justify-content: center;
  }
  .card {
    position: relative;
    width: 1000px; height: 580px;
    background: var(--paper);
    overflow: hidden;
    box-shadow: 0 6px 24px rgba(0,0,0,0.12);
  }
  .identity {
    position: absolute; left: 132px; top: 62px;
    color: var(--ink);
  }
  .identity__name {
    font-size: 74px; line-height: 1; letter-spacing: -1px; font-weight: 400;
  }
  .identity__first { color: var(--sky); font-weight: 700; }
  .identity__role {
    font-size: 40px; line-height: 1; margin-top: 4px; margin-left: -6px; font-weight: 400;
  }
  .company-band {
    position: absolute; left: 0; top: 222px;
    width: 620px; height: 58px;
    background: var(--sky);
    color: var(--paper);
    font-size: 34px; font-weight: 700;
    line-height: 58px;
    padding-left: 100px;
  }
  .contact {
    position: absolute; left: 82px; top: 300px;
    color: var(--ink);
    font-size: 27px; line-height: 38px;
    list-style: none;
  }
  .contact li:first-child { padding-left: 18px; }
  .contact li:nth-child(2) { padding-left: 10px; }
  .contact__label { font-weight: 700; }
  .photo-band {
    position: absolute; left: 820px; top: 330px;
    width: 180px; height: 52px;
    background: var(--sky);
  }
  .portrait {
    position: absolute; left: 600px; top: 196px;
    width: 260px; height: 296px;
    border: 7px solid var(--sky);
    background: var(--paper);
    padding: 10px;
  }
  .portrait__fill {
    width: 100%; height: 100%;
    background: linear-gradient(180deg, var(--photo-light) 0%, var(--photo-mid) 30%, var(--photo-dark) 52%, var(--photo-light) 85%);
  }
  .web-tab {
    position: absolute; left: 205px; top: 468px;
    width: 430px; height: 160px;
    background: var(--sky);
    border-radius: 80px 80px 0 0;
    color: var(--paper);
    font-size: 30px;
    text-align: center;
    padding-top: 26px;
  }
  .web-tab strong { font-weight: 700; }
</style>
</head>
<body>
<main class="stage">
  <article class="card">
    <header class="identity">
      <h1 class="identity__name"><span class="identity__first">Wyn</span> Marchetti</h1>
      <p class="identity__role">Resume Writer</p>
    </header>

    <div class="company-band">Clear Path CVs</div>

    <ul class="contact">
      <li>27 The Lanyard HARWOOD NSW 2465</li>
      <li>wyn@clearpathcvs.com.au</li>
      <li><span class="contact__label">Call:</span> 0417362958</li>
    </ul>

    <div class="photo-band"></div>
    <figure class="portrait">
      <div class="portrait__fill" role="img" aria-label="Portrait photo of Wyn Marchetti"></div>
    </figure>

    <div class="web-tab">www.<strong>clearpathcvs</strong>.com.au</div>
  </article>
</main>
</body>
</html>
```